Brochure & Flyer Design

Coral Skipper Elmgrove - Fish & Chips is a popular fish and chip store located on Sydney’s beautiful northern beaches. It sits just across from the sandy shores of Newport Beach.
Please see attached:
1. Details on the brochure I would like designed for Coral Skipper Elmgrove
2. Current menu that is in store that will need to be included
3. Logo
I would like a modern, fresh design to complement the logo focusing on the food.
Here is the link to download the images that should be included in the brochure https://www.filedrift.net/fetch/PxKmTzQaVbRnLwYcJdHsKe
To complement the brochure I would like an A1 flyer template that can be used to promote specials at the store.

```html
<!DOCTYPE html>
<html lang="en">
<head>
<meta charset="utf-8">
<title>Coral Skipper Elmgrove - Fish &amp; Chips Menu</title>
<link href="https://fonts.googleapis.com/css2?family=Cabin:wght@400;600;700&family=Italianno&family=Baloo+2:wght@700&display=swap" rel="stylesheet">
<style>
  :root {
    --red-core: #d8261f;
    --red-edge: #4a0907;
    --green-core: #1f8a3a;
    --green-edge: #0a3a16;
    --gold-core: #e8a81e;
    --gold-edge: #3a1c07;
    --cream: #f5e6c2;
    --cream-light: #fbf2d8;
    --label-red: #b1202a;
    --label-brown: #8a5a1c;
    --pack-title: #cde34b;
    --ring: #2a8f3c;
    --ring-dark: #16652a;
    --ink-dark: #4a3418;
  }
  * { margin: 0; padding: 0; box-sizing: border-box; }
  html, body { width: 1200px; height: 848px; overflow: hidden; background: #fff; }
  body { font-family: "Cabin", sans-serif; }
  .brochure { position: relative; width: 1200px; height: 848px; display: flex; }
  .panel { position: relative; width: 400px; height: 848px; overflow: hidden; color: var(--cream); }
  .panel--meals { background: radial-gradient(ellipse at 45% 45%, var(--red-core) 0%, #a3140f 50%, var(--red-edge) 100%); }
  .panel--packs { background: radial-gradient(ellipse at 50% 50%, var(--green-core) 0%, #14602a 55%, var(--green-edge) 100%); border-left: 1px solid #0d3a18; border-right: 1px solid #3a2a10; }
  .panel--burgers { background: radial-gradient(ellipse at 55% 55%, var(--gold-core) 0%, #b8720f 45%, var(--gold-edge) 100%); }

  .section-label {
    position: absolute; left: 100px; width: 200px; height: 36px; z-index: 2;
    background: var(--cream-light); border: 2px solid #c9a766;
    border-radius: 4px; display: flex; align-items: center; justify-content: center;
    font-family: "Italianno", cursive; font-size: 32px; line-height: 1; color: var(--label-red);
    box-shadow: 0 0 0 3px rgba(245,230,194,0.35);
  }
  .section-label::before, .section-label::after {
    content: ""; position: absolute; top: 16px; width: 26px; height: 2px; background: var(--cream-light);
  }
  .section-label::before { left: -30px; }
  .section-label::after { right: -30px; }
  .panel--burgers .section-label { color: var(--label-brown); }

  .menu { position: absolute; left: 43px; width: 308px; font-size: 14.5px; line-height: 19px; z-index: 2; }
  .menu-item { margin-bottom: 17px; }
  .menu-row { display: flex; justify-content: space-between; font-weight: 700; }
  .menu-desc { font-weight: 400; }
  .menu-plain { font-weight: 700; }

  .photo { position: absolute; z-index: 0; }
  .photo--burger { left: 0; top: 545px; width: 400px; height: 303px;
    background: radial-gradient(ellipse at 50% 40%, #e6b871 0%, #c98a3a 45%, #7a8f3c 75%, #5a1308 100%);
    border-radius: 48% 52% 0 0 / 30% 30% 0 0; }
  .photo--prawns { left: 870px; top: 655px; width: 330px; height: 193px;
    background: radial-gradient(ellipse at 50% 70%, rgba(214,128,52,0.95) 0%, rgba(197,106,40,0.8) 35%, rgba(240,217,138,0.45) 65%, rgba(240,217,138,0) 100%); }

  .packs-art { position: absolute; left: 0; top: 0; }
  .pack-caption { position: absolute; width: 170px; text-align: center; font-size: 12px; line-height: 15px; color: var(--cream); }
  .pack-caption--bold { font-weight: 700; }
  .pack-price { display: block; font-size: 19px; font-weight: 700; line-height: 26px; margin-top: 2px; }

  .combo {
    position: absolute; left: 870px; top: 333px; width: 262px; height: 72px; z-index: 2;
    background: var(--cream-light); border: 2px solid #c9a766; border-radius: 10px;
    text-align: center; color: var(--ink-dark); font-size: 13.5px; line-height: 18px; padding-top: 9px;
  }
  .combo-title { font-weight: 700; font-size: 14px; color: #5a4a30; }
  .pack-list { position: absolute; left: 846px; width: 306px; top: 480px; z-index: 2; font-size: 14.5px; line-height: 18.9px; font-weight: 700; color: var(--cream); text-shadow: 0 1px 2px rgba(60,30,5,0.6); }
  .pack-list li { list-style: none; display: flex; justify-content: space-between; }
</style>
</head>
<body>
<main class="brochure">

  <section class="panel panel--meals">
    <div class="section-label" style="top:66px;">Family Meals</div>
    <div class="menu" style="top:116px;">
      <div class="menu-item">
        <div class="menu-row"><span>FISHERMANS BASKET</span><span>$ 39.90</span></div>
        <div class="menu-desc">2 Fillets of Fish, 6 Calamari<br>Rings, 4 Prawns, 4 Sea Scallops,<br>Large Chips, Lemon &amp; Sauce</div>
      </div>
      <div class="menu-item">
        <div class="menu-row"><span>DINNER PACK</span><span>$ 42.90</span></div>
        <div class="menu-desc">4 Fillets of Fish, 12 Calamari<br>Rings, Large Chips, Lemon &amp; Sauce</div>
      </div>
    </div>

    <div class="section-label" style="top:292px;">Daily Market Fish</div>
    <div class="menu" style="top:339px;">
      <div class="menu-row"><span>GRILLED OR FRIED</span><span>$ 16.90</span></div>
      <div class="menu-plain">Salmon</div>
      <div class="menu-plain">Barramundi</div>
      <div class="menu-plain">Snapper</div>
      <div class="menu-row"><span>WITH CHIPS</span><span>$ 19.90</span></div>
    </div>

    <div class="section-label" style="top:457px;">Salads</div>
    <div class="menu" style="top:502px;">
      <div class="menu-row"><span>Coleslaw Salad</span><span>$ 6.90</span></div>
      <div class="menu-row"><span>Garden Salad</span><span>$ 6.90</span></div>
    </div>

    <div class="photo photo--burger" role="img" aria-label="Photo of a fish burger with sesame bun, melted cheese and salad"></div>
  </section>

  <section class="panel panel--packs">
    <svg class="packs-art" width="400" height="848" viewBox="400 0 400 848">
      <defs>
        <radialGradient id="pack-photo" cx="50%" cy="45%" r="60%">
          <stop offset="0%" stop-color="#f3ead2"/>
          <stop offset="55%" stop-color="#e2b46a"/>
          <stop offset="100%" stop-color="#c9d3df"/>
        </radialGradient>
        <path id="arc-1" d="M419,150 A95,95 0 0 1 609,150"/>
        <path id="arc-2" d="M591,150 A95,95 0 0 1 781,150"/>
        <path id="arc-3" d="M419,410 A95,95 0 0 1 609,410"/>
        <path id="arc-4" d="M591,410 A95,95 0 0 1 781,410"/>
        <path id="arc-5" d="M419,680 A95,95 0 0 1 609,680"/>
        <path id="arc-6" d="M591,680 A95,95 0 0 1 781,680"/>
      </defs>
      <g class="pack-rings" fill="var(--ring)" stroke="var(--ring-dark)" stroke-width="3" stroke-dasharray="6 4">
        <circle cx="514" cy="150" r="76"/><circle cx="686" cy="150" r="76"/>
        <circle cx="514" cy="410" r="76"/><circle cx="686" cy="410" r="76"/>
        <circle cx="514" cy="680" r="76"/><circle cx="686" cy="680" r="76"/>
      </g>
      <g fill="none" stroke="#fff" stroke-width="4">
        <circle cx="514" cy="150" r="60"/><circle cx="686" cy="150" r="60"/>
        <circle cx="514" cy="410" r="60"/><circle cx="686" cy="410" r="60"/>
        <circle cx="514" cy="680" r="60"/><circle cx="686" cy="680" r="60"/>
      </g>
      <g fill="url(#pack-photo)">
        <circle cx="514" cy="150" r="58" role="img" aria-label="Photo of fish cocktails and chips in a takeaway box"/>
        <circle cx="686" cy="150" r="58" role="img" aria-label="Photo of junior pack with calamari rings, chips and lemon"/>
        <circle cx="514" cy="410" r="58" role="img" aria-label="Photo of calamari rings and chips in a takeaway box"/>
        <circle cx="686" cy="410" r="58" role="img" aria-label="Photo of a battered fish fillet and chips with lemon"/>
        <circle cx="514" cy="680" r="58" role="img" aria-label="Photo of prawns and chips in a takeaway box"/>
        <circle cx="686" cy="680" r="58" role="img" aria-label="Photo of sea scallops and chips with lemon"/>
      </g>
      <g font-family="'Baloo 2', 'Cabin', sans-serif" font-weight="700" font-size="17" fill="var(--pack-title)" letter-spacing="1" text-anchor="middle">
        <text><textPath href="#arc-1" startOffset="50%">FISH COCKTAIL PACK</textPath></text>
        <text><textPath href="#arc-2" startOffset="50%">JUNIOR PACK</textPath></text>
        <text><textPath href="#arc-3" startOffset="50%">CALAMARI PACK</textPath></text>
        <text><textPath href="#arc-4" startOffset="50%">FISH &amp; CHIPS</textPath></text>
        <text><textPath href="#arc-5" startOffset="50%">PRAWN PACK</textPath></text>
        <text><textPath href="#arc-6" startOffset="50%">SEA SCALLOP PACK</textPath></text>
      </g>
    </svg>

    <p class="pack-caption pack-caption--bold" style="left:29px; top:231px;">6 Fish Cocktails and Chips<span class="pack-price">$ 13.90</span></p>
    <p class="pack-caption" style="left:201px; top:231px;">2 Fish Cocktails,<br>2 Calamari Rings,<br>1 Seafood Stick and Chips<span class="pack-price">$ 9.90</span></p>
    <p class="pack-caption" style="left:29px; top:493px;">8 Calamari Rings and Chips<span class="pack-price">$ 11.90</span></p>
    <p class="pack-caption" style="left:201px; top:493px;">1 Fillet of Fish and Chips<span class="pack-price">$ 11.90</span></p>
    <p class="pack-caption" style="left:29px; top:754px;">6 Prawns and Chips<span class="pack-price">$ 14.50</span></p>
    <p class="pack-caption" style="left:201px; top:754px;">6 Sea Scallops and Chips<span class="pack-price">$ 14.50</span></p>
  </section>

  <section class="panel panel--burgers">
    <div class="section-label" style="top:66px;">Burgers</div>
    <div class="menu" style="top:116px; left:45px; width:306px;">
      <div class="menu-item" style="margin-bottom:4px;">
        <div class="menu-row"><span>Outrigger Burger</span><span>$ 7.90</span></div>
        <div class="menu-desc">4 Calamari Rings,<br>Garden Lettuce &amp; Tartare Sauce</div>
      </div>
      <div class="menu-item" style="margin-bottom:4px;">
        <div class="menu-row"><span>Odessey Burger</span><span>$ 7.90</span></div>
        <div class="menu-desc">Fish Fillet, Coleslaw Salad &amp;<br>Seafood Sauce</div>
      </div>
      <div class="menu-item" style="margin-bottom:4px;">
        <div class="menu-row"><span>Olympiad Burger</span><span>$ 7.90</span></div>
        <div class="menu-desc">Fish Fillet, Fresh Tomato,<br>Garden Lettuce &amp; Tartare Sauce</div>
      </div>
      <div class="menu-plain">Grilled + $ 2</div>
    </div>
  </section>

  <div class="photo photo--prawns" role="img" aria-label="Photo of battered prawns with chips and a lemon wedge"></div>

  <div class="combo">
    <div class="combo-title">BURGER COMBO$ 12.90</div>
    Choose any burger with chips and<br>600ml water
  </div>

  <div class="section-label" style="top:430px; left:900px; color:var(--label-brown);">Create a Pack</div>
  <ul class="pack-list">
    <li><span>Fillet of Fish</span><span>$ 8.90</span></li>
    <li><span>Fish Cocktail</span><span>$ 2.40</span></li>
    <li><span>Calamari Ring</span><span>$ 1.0</span></li>
    <li><span>Prawn Cutlet</span><span>$ 2.40</span></li>
    <li><span>Sea Scallop</span><span>$ 2.40</span></li>
    <li><span>Ocean Mussel</span><span>$ 1.00</span></li>
    <li><span>Seafood Stick</span><span>$ 1.80</span></li>
    <li><span>Small Chips</span><span>$ 4.50</span></li>
    <li><span>Large Chips</span><span>$ 7.00</span></li>
    <li><span>Potato Scallop</span><span>$ 1.00</span></li>
    <li><span>Banana Fritter</span><span>$ 3.00</span></li>
    <li><span>Pineapple Fritter</span><span>$ 3.00</span></li>
    <li><span>Vegie Spring Roll</span><span>$ 2.50</span></li>
    <li><span>Extra Sauce</span><span>50 c</span></li>
  </ul>
</main>
</body>
</html>
```